Lantern Marketing Group (LMG)

This is for my business cards. I want a Nice anfd Elegant Business Card to be Designed, Using more or less of the same colors of my logo that i have attached.i would like to have these business cards forever

Thank you

Thank you

Thank you

Contact Information for Business Card

Calvin Ortega
Lantern Marketing Group
C.(555) 482-1306
E-Mail. COrtega@lanternmgroup.example

Font styles to use
Serif
Sans Serif

Colors
d0dfed
cbcbcb
cee9f5

Requirements
Must have
• (LMG)
• Lantern Marketing Group
Nice to have
• 3D affects
Should not have
• Please try not using the flat version of the logo try and use the 3d version please

```html
<!DOCTYPE html>
<html lang="en">
<head>
<meta charset="utf-8">
<title>Lantern Marketing Group – Business Card</title>
<link rel="stylesheet" href="https://fonts.googleapis.com/css2?family=Lato:wght@400;700&display=swap">
<style>
  :root {
    --backdrop: #161616;
    --card: #0b0b0c;
    --card-edge: #1c1c1e;
    --accent: #2a8fd6;
    --accent-light: #3fa9e8;
    --text-light: #f2f4f6;
    --text-muted: #cbcbcb;
  }
  * { box-sizing: border-box; margin: 0; padding: 0; }
  html, body {
    width: 1200px; height: 864px; overflow: hidden;
    background: var(--backdrop);
    font-family: "Lato", sans-serif;
  }
  .sheet {
    width: 1200px; height: 864px;
    display: flex; flex-direction: column;
    align-items: center; justify-content: center; gap: 44px;
  }
  .card {
    position: relative;
    width: 600px; height: 344px;
    border-radius: 22px;
    background: linear-gradient(160deg, var(--card-edge) 0%, var(--card) 55%);
    overflow: hidden;
  }
  /* back side */
  .card-back {
    display: flex; align-items: center; justify-content: center; gap: 14px;
  }
  .brand-square {
    width: 26px; height: 26px; background: var(--accent);
  }
  .brand-name {
    font-weight: 700; font-size: 30px; letter-spacing: 1px;
    text-transform: uppercase; color: var(--accent-light);
  }
  /* front side */
  .edge-bar {
    position: absolute; top: 40px; bottom: 40px; width: 12px;
    border-radius: 6px;
    background: linear-gradient(180deg, var(--accent-light), var(--accent));
  }
  .edge-bar.left { left: 0; border-radius: 0 6px 6px 0; }
  .edge-bar.right { right: 0; border-radius: 6px 0 0 6px; }
  .contact {
    position: absolute; left: 60px; top: 104px;
  }
  .person-name {
    font-weight: 700; font-size: 18px; color: var(--text-light);
    text-transform: uppercase; letter-spacing: 0.3px;
  }
  .company-name {
    font-size: 15px; color: var(--accent-light);
    text-transform: uppercase; margin-top: 2px;
  }
  .contact-line {
    display: flex; align-items: center; gap: 9px;
    font-size: 14px; color: var(--text-light);
    margin-top: 10px;
  }
  .contact-line:first-of-type { margin-top: 18px; }
  .contact-line svg { width: 14px; height: 14px; fill: var(--accent-light); }
  .divider {
    position: absolute; left: 340px; top: 108px; height: 128px;
    width: 1px; background: var(--accent);
  }
  .front-mark {
    position: absolute; left: 380px; top: 0; bottom: 0; width: 180px;
    display: flex; align-items: center; justify-content: center;
    font-weight: 700; font-size: 64px; color: var(--accent-light);
    letter-spacing: 2px;
  }
</style>
</head>
<body>
<main class="sheet">
  <section class="card card-back" aria-label="Card back">
    <span class="brand-square"></span>
    <span class="brand-name">Lantern Marketing Group</span>
  </section>

  <section class="card card-front" aria-label="Card front">
    <span class="edge-bar left"></span>
    <span class="edge-bar right"></span>
    <div class="contact">
      <p class="person-name">Calvin Ortega</p>
      <p class="company-name">Lantern Marketing Group</p>
      <p class="contact-line">
        <svg viewBox="0 0 16 16" aria-hidden="true"><path d="M3.6 1.5l2.3 2.6-1.3 1.8c.9 2 2.5 3.6 4.5 4.5l1.8-1.3 2.6 2.3-1.4 2.1C7 14 2 9 1.5 2.9z"/></svg>
        (555) 482-1306
      </p>
      <p class="contact-line">
        <svg viewBox="0 0 16 16" aria-hidden="true"><path d="M1 3h14v10H1z M2 4.2v.5l6 4 6-4v-.5z" fill-rule="evenodd"/></svg>
        COrtega@lanternmgroup.example
      </p>
    </div>
    <span class="divider"></span>
    <div class="front-mark">LMG</div>
  </section>
</main>
</body>
</html>
```